Business Card Design Project

Business Card
We are rebranding with a new logo
Industry/Entity Type
Business
Contact Information for Business Card
Dennis Marlow +61 427581962 dennis@qovo.com.au P.O. Box 872 Kelvindale QLD 4309
Requirements
Must have
- Logo

```html
<!DOCTYPE html>
<html lang="en">
<head>
<meta charset="utf-8">
<title>Qovo International – Business Card</title>
<link rel="stylesheet" href="https://fonts.googleapis.com/css2?family=Exo+2:wght@400;500&display=swap">
<style>
  :root {
    --backdrop: #e9e9e9;
    --card: #ffffff;
    --blue: #1a82c4;
    --orange: #ef6a1f;
    --orange-light: #f7931e;
    --orange-deep: #e4541f;
    --grey: #7d7d7d;
  }
  * { margin: 0; padding: 0; box-sizing: border-box; }
  html, body {
    width: 1200px;
    height: 801px;
    overflow: hidden;
    background: var(--backdrop);
    font-family: "Exo 2", sans-serif;
  }
  .business-card {
    position: absolute;
    left: 180px;
    top: 160px;
    width: 840px;
    height: 480px;
    background: var(--card);
    box-shadow: 0 6px 24px rgba(0, 0, 0, 0.12);
    overflow: hidden;
  }
  .holder-name {
    position: absolute;
    left: 96px;
    top: 132px;
    padding-left: 22px;
    border-left: 6px solid var(--orange);
    color: var(--blue);
    font-size: 24px;
    font-weight: 500;
    line-height: 1.05;
    letter-spacing: 0.5px;
    text-transform: uppercase;
  }
  .brand {
    position: absolute;
    right: 110px;
    top: 86px;
    display: flex;
    align-items: center;
    gap: 12px;
  }
  .brand-mark {
    width: 16px;
    height: 16px;
    border-radius: 50%;
    background: var(--orange);
  }
  .brand-name {
    color: var(--blue);
    font-size: 30px;
    font-weight: 500;
    letter-spacing: 1px;
  }
  .postal-address {
    position: absolute;
    left: 590px;
    top: 300px;
    color: var(--grey);
    font-size: 17px;
    line-height: 1.3;
  }
  .contact-list {
    position: absolute;
    left: 170px;
    top: 372px;
    list-style: none;
    color: var(--grey);
    font-size: 17px;
    line-height: 1.35;
  }
  .contact-label { color: var(--orange); }
  .brand-band {
    position: absolute;
    left: 0;
    right: 0;
    bottom: 0;
    height: 10px;
    display: flex;
  }
  .band-light { flex: 40; background: linear-gradient(90deg, var(--orange-light), #f28220); }
  .band-deep  { flex: 30; background: var(--orange-deep); }
  .band-blue  { flex: 30; background: var(--blue); }
</style>
</head>
<body>
  <article class="business-card">
    <h1 class="holder-name">Dennis<br>Marlow</h1>

    <div class="brand">
      <span class="brand-mark"></span>
      <span class="brand-name">Qovo International</span>
    </div>

    <address class="postal-address">
      P.O. Box 872<br>
      Kelvindale QLD 4309
    </address>

    <ul class="contact-list">
      <li><span class="contact-label">Cell:</span> +61 427581962</li>
      <li><span class="contact-label">Email:</span> dennis@qovo.com.au</li>
    </ul>

    <div class="brand-band">
      <span class="band-light"></span>
      <span class="band-deep"></span>
      <span class="band-blue"></span>
    </div>
  </article>
</body>
</html>
```